Revamp QuillStoneKit.com

https://quillstonekit.com/ needs a revamp. We like the general style and colors of the site, we just want to modernize the landing page, product page, view cart page, and the final confirm page.

I'm just looking for the PSD (Photoshop files) as the deliverable.

Quick Summary
Please redesign the following Pages:
1) https://quillstonekit.com/
2) https://quillstonekit.com/rubberTracks/QuillStoneKit/400x725nx70.php (product Page)
3) https://quillstonekit.com/viewCart.php (view cart - Add something to cart to see)
4) https://quillstonekit.com/confirmShoppingCart.php (confirm cart - Add something to cart to see)

```html
<!DOCTYPE html>
<html lang="en">
<head>
<meta charset="utf-8">
<title>QuillStoneKit — Rubber Tracks</title>
<link href="https://fonts.googleapis.com/css2?family=Saira+Condensed:wght@400;500;600;700&family=Open+Sans:wght@400;600&display=swap" rel="stylesheet">
<style>
:root{
  --gold:#d9a92c;
  --ink:#1d1f24;
  --dark:#24262b;
  --text:#3a3a3a;
  --muted:#9a9a9a;
  --line:#e6e6e6;
  --white:#ffffff;
  --footer:#2b2d33;
}
*{box-sizing:border-box;margin:0;padding:0}
html,body{width:1200px;height:3478px;overflow:hidden;background:var(--white)}
body{font-family:"Open Sans",sans-serif;color:var(--text);position:relative}
.cond{font-family:"Saira Condensed",sans-serif}

/* header */
.topbar{position:absolute;left:0;top:0;width:1200px;height:34px;background:var(--dark);color:#ddd;font-family:"Saira Condensed",sans-serif;font-size:14px;display:flex;justify-content:flex-end;align-items:center;padding-right:80px;gap:20px}
.topbar span{display:flex;align-items:center;gap:6px}
.nav{position:absolute;left:0;top:34px;width:1200px;height:58px;background:var(--white);box-shadow:0 1px 3px rgba(0,0,0,.08)}
.brand{position:absolute;left:0;top:0;width:330px;height:92px;background:var(--gold);clip-path:polygon(0 0,100% 0,78% 100%,0 100%);z-index:3;display:flex;align-items:center;padding-left:82px;font-family:"Saira Condensed",sans-serif;font-weight:700;font-size:30px;color:var(--white);letter-spacing:.5px}
.menu{position:absolute;left:328px;top:0;height:58px;display:flex;align-items:center;gap:24px;font-family:"Saira Condensed",sans-serif;font-size:14px;font-weight:600;color:#333;letter-spacing:.6px}
.tools{position:absolute;right:80px;top:0;height:58px;display:flex;align-items:center;gap:28px}
.badge{position:absolute;top:-8px;right:-9px;width:16px;height:16px;border-radius:50%;background:#e24a3b;color:#fff;font-size:10px;display:flex;align-items:center;justify-content:center}

/* hero */
.hero{position:absolute;left:0;top:92px;width:1200px;height:630px;background:radial-gradient(ellipse at 70% 60%,#6a4a1c 0%,#3a2c18 35%,#1b1c20 75%)}
.hero-copy{position:absolute;left:84px;top:188px;font-family:"Saira Condensed",sans-serif}
.hero-copy .a{color:var(--gold);font-size:66px;font-weight:700;line-height:1}
.hero-copy .b{color:var(--white);font-size:66px;font-weight:700;line-height:1;margin-top:14px}
.hero-copy .rule{width:514px;height:3px;background:var(--gold);margin:22px 0 24px 2px}
.hero-copy .c{color:var(--white);font-size:40px;letter-spacing:1px;line-height:1}

/* promo cards */
.promo{position:absolute;top:759px;width:496px;height:282px;background:linear-gradient(135deg,#3b3328,#2a2620 60%,#4b3a22)}
.promo .t1{position:absolute;left:20px;top:50px;font-family:"Saira Condensed",sans-serif;font-size:48px;font-weight:700;color:var(--gold);line-height:1}
.promo .t2{position:absolute;left:20px;top:96px;font-family:"Saira Condensed",sans-serif;font-size:48px;font-weight:700;color:var(--white);line-height:1}
.promo .rule{position:absolute;left:12px;top:160px;width:176px;height:2px;background:var(--gold)}
.promo .t3{position:absolute;left:15px;top:172px;font-family:"Saira Condensed",sans-serif;font-size:30px;color:var(--white);letter-spacing:.5px}

/* product rows */
.row{position:absolute;left:84px;width:1032px;display:grid;grid-template-columns:repeat(4,1fr);border-bottom:4px solid var(--line)}
.card{position:relative;height:303px;text-align:center}
.card+.card::before{content:"";position:absolute;left:0;top:58px;height:230px;width:1px;background:#f0f0f0}
.shot{width:140px;height:92px;margin:16px auto 0;border-radius:4px;background:linear-gradient(160deg,#f1d16a,#c9a13a 45%,#2b2b2b)}
.shot.white{background:linear-gradient(160deg,#f3f3f3,#cfcfcf 55%,#3a3a3a)}
.shot.dark{background:linear-gradient(160deg,#d7b548,#4a4a4a 50%,#1c1c1c)}
.pname{font-family:"Saira Condensed",sans-serif;font-size:26px;color:#333;margin-top:22px;letter-spacing:.5px}
.stars{font-size:8px;color:var(--gold);letter-spacing:1px;margin-top:6px}
.stars i{color:#ccc;font-style:normal}
.price{font-family:"Saira Condensed",sans-serif;font-size:17px;color:#333;margin-top:10px}
.specs{position:absolute;left:20px;right:10px;top:242px;border-top:1px solid #eee;display:flex;justify-content:space-between;padding-top:10px;font-family:"Saira Condensed",sans-serif;font-size:11px;color:var(--muted)}
.specs span{display:flex;flex-direction:column;align-items:center;gap:4px;width:33%}
.specs b{width:8px;height:8px;border-radius:50%;background:#d0d0d0;display:block}

/* bands */
.band{position:absolute;left:0;width:1200px;background:linear-gradient(90deg,#2a2520,#1d1d20 40%,#221f1c);display:flex;align-items:center;justify-content:center;font-family:"Saira Condensed",sans-serif;font-size:64px;color:var(--white);letter-spacing:.5px}
.band em{font-style:normal;font-weight:700;color:var(--gold);margin-right:14px}

/* brands */
.brands{position:absolute;left:84px;top:2703px;width:1032px;height:420px;display:grid;grid-template-columns:repeat(4,1fr);grid-template-rows:1fr 1fr}
.brands div{display:flex;align-items:center;justify-content:center;font-family:"Saira Condensed",sans-serif;font-weight:700;font-size:40px;letter-spacing:1px;color:#333}
.brands div:nth-child(-n+4){border-bottom:1px dashed #bbb}
.brands div:not(:nth-child(4n+1)){border-left:1px dashed #bbb}

/* footer */
.footer{position:absolute;left:0;top:3158px;width:1200px;height:320px;background:var(--footer);color:#d5d5d5}
.f-brand{position:absolute;left:88px;top:30px;font-family:"Saira Condensed",sans-serif;font-weight:700;font-size:28px;color:var(--white)}
.f-info{position:absolute;left:98px;top:92px;font-size:10.5px;line-height:15px}
.f-info p{margin-bottom:18px}
.f-col{position:absolute;top:56px}
.f-col h4{font-family:"Saira Condensed",sans-serif;font-size:15px;font-weight:600;color:var(--white);letter-spacing:.5px;margin-bottom:14px}
.f-col li{list-style:none;font-size:10.5px;line-height:22.5px}
.f-bottom{position:absolute;left:0;top:257px;width:1200px;height:63px;border-top:1px solid #3d3f46;display:flex;align-items:center}
.social{position:absolute;left:85px;display:flex;gap:6px}
.social span{width:30px;height:28px;background:#3b5998;display:block}
.copy{position:absolute;left:450px;font-family:"Saira Condensed",sans-serif;font-size:15px;color:#cfcfcf}
</style>
</head>
<body>

<header>
  <div class="topbar">
    <span><svg width="11" height="11" viewBox="0 0 12 12"><circle cx="6" cy="6" r="5" fill="none" stroke="#ccc" stroke-width="1.4"/><path d="M6 3v3l2 1" stroke="#ccc" stroke-width="1.2" fill="none"/></svg>Mon - Fri : 09am to 06pm</span>
    <span><svg width="11" height="11" viewBox="0 0 12 12"><path d="M2 1l2.5 0 1 3-1.5 1a7 7 0 0 0 3 3l1-1.5 3 1V10a1 1 0 0 1-1 1A9 9 0 0 1 1 2a1 1 0 0 1 1-1z" fill="#ccc"/></svg>+1 800 555 0142</span>
  </div>
  <div class="brand">QuillStoneKit</div>
  <nav class="nav">
    <div class="menu"><span>HOME</span><span>ACCESSORIES</span><span>LISTING</span><span>BLOG</span><span>COMPARE CARS</span><span>PAGES</span><span>CUSTOM</span></div>
    <div class="tools">
      <svg width="15" height="15" viewBox="0 0 16 16"><circle cx="6.5" cy="6.5" r="5" fill="none" stroke="#222" stroke-width="2"/><path d="M10.5 10.5l4 4" stroke="#222" stroke-width="2"/></svg>
      <span style="position:relative"><svg width="22" height="20" viewBox="0 0 22 20"><path d="M1 2h4l3 11h10l2-8H7" fill="none" stroke="#222" stroke-width="2"/><circle cx="9" cy="17" r="1.7" fill="#222"/><circle cx="17" cy="17" r="1.7" fill="#222"/></svg><span class="badge">2</span></span>
      <svg width="14" height="12" viewBox="0 0 14 12"><path d="M0 1h14M0 6h14M0 11h14" stroke="#222" stroke-width="2"/></svg>
    </div>
  </nav>
</header>

<section class="hero" role="img" aria-label="Photo of a yellow wheel loader at dusk">
  <div class="hero-copy">
    <div class="a">HIGH QUALITY</div>
    <div class="b">REPLACEMENT RUBBER TRACKS</div>
    <div class="rule"></div>
    <div class="c">DELIVERED TO YOUR DOOR</div>
  </div>
</section>

<div class="promo" style="left:85px" role="img" aria-label="Photo of an orange crawler excavator">
  <div class="t1">Crawler Digger</div><div class="t2">Loader</div><div class="rule"></div><div class="t3">Replacement Rubber Tracks</div>
</div>
<div class="promo" style="left:618px" role="img" aria-label="Photo of a yellow crawler excavator">
  <div class="t1">Crawler Digger</div><div class="t2">Loader</div><div class="rule"></div><div class="t3">Replacement Rubber Tracks</div>
</div>

<section class="row" style="top:1110px">
  <div class="card"><div class="shot white" role="img" aria-label="White skid steer loader"></div><div class="pname">Product name</div><div class="stars">★★★★<i>★</i></div><div class="price">$49000.00</div><div class="specs"><span><b></b>4875km</span><span><b></b>Automatic</span><span><b></b>2018</span></div></div>
  <div class="card"><div class="shot dark" role="img" aria-label="Tracked forestry mulcher"></div><div class="pname">Product name</div><div class="stars">★★★★<i>★</i></div><div class="price">$39000.00</div><div class="specs"><span><b></b>847km</span><span><b></b>Manual</span><span><b></b>2018</span></div></div>
  <div class="card"><div class="shot" role="img" aria-label="Yellow compact track loader"></div><div class="pname">Product name</div><div class="stars">★★★★<i>★</i></div><div class="price">$99000.00</div><div class="specs"><span><b></b>687km</span><span><b></b>Manual</span><span><b></b>2019</span></div></div>
  <div class="card"><div class="shot dark" role="img" aria-label="Tracked forestry mulcher"></div><div class="pname">Product name</div><div class="stars">★★★★<i>★</i></div><div class="price">$59000.00</div><div class="specs"><span><b></b>10587km</span><span><b></b>Manual</span><span><b></b>2017</span></div></div>
</section>

<section class="band" style="top:1452px;height:282px" role="img" aria-label="Dark photo of a tracked machine on a farm"><span><em>FARM TOUGH</em>RUBBER TRACKS</span></section>

<section class="row" style="top:1772px">
  <div class="card"><div class="shot white" role="img" aria-label="White skid steer loader"></div><div class="pname">Product name</div><div class="stars">★★★★<i>★</i></div><div class="price">$49000.00</div><div class="specs"><span><b></b>4875km</span><span><b></b>Automatic</span><span><b></b>2018</span></div></div>
  <div class="card"><div class="shot dark" role="img" aria-label="Tracked forestry mulcher"></div><div class="pname">Product name</div><div class="stars">★★★★<i>★</i></div><div class="price">$39000.00</div><div class="specs"><span><b></b>847km</span><span><b></b>Manual</span><span><b></b>2018</span></div></div>
  <div class="card"><div class="shot" role="img" aria-label="Yellow compact track loader"></div><div class="pname">Product name</div><div class="stars">★★★★<i>★</i></div><div class="price">$99000.00</div><div class="specs"><span><b></b>687km</span><span><b></b>Manual</span><span><b></b>2019</span></div></div>
  <div class="card"><div class="shot dark" role="img" aria-label="Tracked forestry mulcher"></div><div class="pname">Product name</div><div class="stars">★★★★<i>★</i></div><div class="price">$59000.00</div><div class="specs"><span><b></b>10587km</span><span><b></b>Manual</span><span><b></b>2017</span></div></div>
</section>

<section class="row" style="top:2083px">
  <div class="card"><div class="shot white" role="img" aria-label="White skid steer loader"></div><div class="pname">Product name</div><div class="stars">★★★★<i>★</i></div><div class="price">$49000.00</div><div class="specs"><span><b></b>4875km</span><span><b></b>Automatic</span><span><b></b>2018</span></div></div>
  <div class="card"><div class="shot dark" role="img" aria-label="Tracked forestry mulcher"></div><div class="pname">Product name</div><div class="stars">★★★★<i>★</i></div><div class="price">$39000.00</div><div class="specs"><span><b></b>847km</span><span><b></b>Manual</span><span><b></b>2018</span></div></div>
  <div class="card"><div class="shot" role="img" aria-label="Yellow compact track loader"></div><div class="pname">Product name</div><div class="stars">★★★★<i>★</i></div><div class="price">$99000.00</div><div class="specs"><span><b></b>687km</span><span><b></b>Manual</span><span><b></b>2019</span></div></div>
  <div class="card"><div class="shot dark" role="img" aria-label="Tracked forestry mulcher"></div><div class="pname">Product name</div><div class="stars">★★★★<i>★</i></div><div class="price">$59000.00</div><div class="specs"><span><b></b>10587km</span><span><b></b>Manual</span><span><b></b>2017</span></div></div>
</section>

<section class="band" style="top:2430px;height:241px" role="img" aria-label="Dark photo of a tracked machine"><span><em>TRACKS BY</em>BRANDS :</span></section>

<section class="brands">
  <div>Torvik</div><div>Ridgeway</div><div>Haulmark</div><div>Brannock</div>
  <div>Furrowline</div><div>Veltaro</div><div>Quarrix</div><div>Stenhold</div>
</section>

<footer class="footer">
  <div class="f-brand">QuillStoneKit</div>
  <div class="f-info">
    <p>Stonefield Co, 214 Elm rd, Harlow,<br>CA 54321 USA</p>
    <p>+1 800 555 0142</p>
    <p>hello@quillstonekit.com</p>
    <p>Mon - Fri : 09am to 06pm</p>
  </div>
  <div class="f-col" style="left:480px"><h4>QUICK LINKS</h4><ul><li>Blog</li><li>FAQs</li><li>Payment</li><li>Shipment</li><li>Where is my order?</li><li>Return policy</li></ul></div>
  <div class="f-col" style="left:696px"><h4>STYLE ADVISOR</h4><ul><li>Your Account</li><li>Information</li><li>Addresses</li><li>Discount</li><li>Orders History</li><li>Additional Information</li></ul></div>
  <div class="f-col" style="left:912px"><h4>INFORMATION</h4><ul><li>Site Map</li><li>Search Terms</li><li>Advanced Search</li><li>About Us</li><li>Contact Us</li><li>Suppliers</li></ul></div>
  <div class="f-bottom">
    <div class="social"><span></span><span style="background:#1da1f2"></span><span style="background:#dd4b39"></span><span style="background:#f39c12"></span><span style="background:#c92228"></span><span style="background:#0e76a8"></span><span style="background:#e52d27"></span></div>
    <div class="copy">2020 QuillStoneKit, LLC. All Rights are Reserved.</div>
  </div>
</footer>

</body>
</html>
```